Amber Ladle Wishes Website Design; Cupcake Business with a unique and bespoke design element

We need a website design for a new bespoke and unique business making gourmet cupcakes - but MOST IMPORTANTLY we design and handmake cupcake wrappers and toppers specifically for each client's event. We are based in Sydney, Australia. The final resulting website should be elegant yet whimsical reflecting the notion of dreams and very elegant events eg weddings and very special parties.

We want to eventually have about 5 pages, HOWEVER, this project is specifically for the first page (ie Home page) and one other only. The final required pages are: a HOME page; ABOUT US page; PHOTO GALLERY page; FLAVOUR MENU & OTHER PRODUCTS page; CONTACT & INTERNET ENQUIRY page.

We expect the HOME page to be quite elaborate, perhaps including some animation. We will be providing the text content for all the other pages, and basically they will have the same background as the home page. We are looking for a clean design that runs across each page thus giving the website a continuity that pulls it all together. We would like our logo to be included on each page.

PLEASE NOTE: We will want multiple pages worked on in the handover phase but initially we want a very concise, consistent template to limit the amount of work to prospective designers.

While we are primarily looking for the design phase to be covered by this project, we would certainly appreciate coding to be included and will take that into consideration when choosing a winner.

Hi Designers

We have added some more information to our brief - please review it.

Thanks and happy designing

Hi Designers

Please note that we have increased our Prize money to $750.00.  We hope this encourages you to participate.

Thanks and regards
Amber Ladle Wishes

Hi Designers

We've just posted some photos to help give you an idea of what we do.  Please note our attention to detail and precision in our work.

Thanks
Amber Ladle Wishes

Hi Designers

Please Note:  What makes us different  to any other cupcake business is that we design cupcake wrappers and toppers, unique to our client's event whether it be a wedding, a birthday party or product launch.  We consult with our client to understand themes, colours, styles etc.  We then have our designs printed, next they are cut by a specialised computerised cutting machine,  We assemble everything by hand, and usually embellish the wrapper and topper with pearls, crystals, feathers, lace, ribbons or whatever else is appropriate for the event.  All work is totally bespoke, unique and individual.  No other cupcake supplier that we know of goes to these lengths to satisfy their client's dreams.

THE WRAPPER AND TOPPER IS OUR PRIMARY SELLING POINT. 

PLEASE NOTE:- We have uploaded a new photograph which we want to be used as the main photograph on the landing page.

We have removed all previous photographs of cupcakes (except for one that we can't get rid of).

We don't want a picture of a cupcake on the landing page we want the image _D7C3239.jpg to be used for that purpose.

We have also uploaded our logo in a number of file formats as we have had requests from you for these.

Hi designers

we have a crazy busy weekend on and won't be able to make any decisions re our competition until Monday  -  sorry to keep you in suspense, just a couple more days please!

regards
Meg

Target Market(s)

Primarily women - brides, new mothers (Christenings), Event Planners, who place an emphasis on the beauty of a product rather than the cost

Industry/Entity Type

Events

Requirements
Must have
• It must have our Logo (see attached upload) on each page (our logo is a butterfly atop a cupcake resting on a spoon and our motto is "Creating Delicious Works of Art". The colours used are pale pink, blue and chocolate brown and we'd expect these colours to be repeated in the final website.
The website must have a photo gallery which we can access and add to/change as our business grows.
We need a contact page which has an "internet enquiry form".
There should be a "Menu" page describing our cupcake flavours.
The Home page must have a party/event feel to it - definitely making an enquirer want to enter further into the site.
Nice to have
• Our logo is attached below in the "uploads". One idea that we have had is to use the butterfly in the logo but start it as a caterpillar crawling on the screen; as it spins it's cocoon the words "Sweet Dreams Little Caterpillar" would appear on screen; this would incorporate the "Dreams" in our Business Name; then our logo butterfly would hatch. This encapsulates the idea of taking something plain (caterpillar/cupcake) and creating something beautiful (butterfly/OUR cupcake).
However, we are open to other design ideas.
The colours we would like to have are pale pink, blue and chocolate brown in the design.

Some websites we really admire are: www.dorawillow.com www.thimblereedtart.com.au and www.greetingsvera.com.au
These websites have a lightness and sense of fantasy to them. They do not convey a corporate image at all, rather they make you want to be at the party.
Should not have
• No "Corporate" style.

Most Important: We already have a website which we are not happy with - that is why we are going through this exercise to replace it. That means we DO NOT want anything along the lines of our current website. We are expecting some fresh ideas for our prize money.

```html
<!DOCTYPE html>
<html lang="en">
<head>
<meta charset="utf-8">
<title>Amber Ladle Wishes</title>
<link href="https://fonts.googleapis.com/css2?family=Oswald:wght@400&family=Lobster+Two:ital,wght@1,700&family=Open+Sans:ital,wght@0,400;1,400&display=swap" rel="stylesheet">
<style>
:root{
  --pink:#f5cbd2;
  --pink-glow:#f8d7dc;
  --choc:#3e201b;
  --choc-text:#4a2822;
  --blue:#6c9cc6;
  --blue-dark:#4f7fab;
  --blue-light:#8db6da;
  --blue-ink:#2f4d6b;
  --cream:#f0e6c8;
  --stone:#d8ccb3;
  --white:#ffffff;
}
*{margin:0;padding:0;box-sizing:border-box}
html,body{width:977px;height:1200px;overflow:hidden}
body{
  position:relative;
  background:radial-gradient(ellipse at 50% 55%,var(--pink-glow),var(--pink) 60%);
  font-family:Arial,Helvetica,sans-serif;
  color:var(--choc-text);
}
.script{font-family:'Lobster Two',cursive;font-style:italic;font-weight:700}
.top-band{position:absolute;left:0;top:0;width:977px;height:18px;background:var(--choc)}
.scallop{position:absolute;left:0;width:977px;height:6px;
  background:radial-gradient(circle at 3px 0,var(--choc) 3px,transparent 3.5px) 0 0/6px 6px repeat-x}
.scallop.down{top:18px}
.scallop.up{top:997px;background:radial-gradient(circle at 3px 6px,var(--choc) 3px,transparent 3.5px) 0 0/6px 6px repeat-x}

.ribbon-tail{position:absolute;background:var(--blue-dark)}
.nav-bar{position:absolute;top:107px;height:36px;background:linear-gradient(var(--blue-light),var(--blue));
  display:flex;align-items:center;box-shadow:0 2px 3px rgba(0,0,0,.2)}
.nav-bar a{font-family:'Oswald',sans-serif;font-size:12.5px;color:var(--blue-ink);text-decoration:none;white-space:nowrap;
  padding:0 11px;border-right:1px solid rgba(47,77,107,.4);line-height:16px;letter-spacing:.2px}
.nav-bar a:last-child{border-right:none}
.nav-left{left:118px;width:257px;padding-left:10px}
.nav-right{left:602px;width:258px;padding-left:6px}

.brand{position:absolute;left:375px;top:10px;width:227px;height:163px;background:var(--stone);
  border:1px solid var(--choc);display:flex;align-items:center;justify-content:center;gap:8px;z-index:3}
.brand-dot{width:10px;height:10px;border-radius:50%;background:var(--choc)}
.brand-name{font-family:'Oswald',sans-serif;font-size:21px;font-weight:400;color:var(--choc);white-space:nowrap}

.hero{position:absolute;left:129px;top:143px;width:716px;height:428px;
  background:linear-gradient(135deg,#5a3e30 0%,#c9b49a 30%,#d8c6ad 50%,#8d7767 70%,#3a302e 100%);
  box-shadow:0 0 0 4px rgba(240,230,215,.7)}
.hero-tag{position:absolute;left:602px;top:466px;width:253px;height:37px;
  background:linear-gradient(var(--blue-light),var(--blue));display:flex;align-items:center;justify-content:center;
  font-size:22px;color:var(--blue-ink);box-shadow:0 2px 3px rgba(0,0,0,.25);z-index:2}

.headline{position:absolute;left:129px;top:578px;width:716px;text-align:center;
  font-size:52px;line-height:60px;color:var(--choc);white-space:nowrap}

.feature{position:absolute;top:676px;width:342px}
.feature.left{left:129px}.feature.right{left:491px}
.feature h2{font-family:'Oswald',sans-serif;font-weight:400;font-size:20px;color:var(--choc);display:flex;align-items:center;gap:6px;margin-bottom:6px;white-space:nowrap}
.feature h2::before{content:"";width:12px;height:12px;border-radius:50%;border:2px solid var(--choc)}
.feature p{font-size:9.3px;line-height:13px;margin-bottom:8px;color:var(--choc-text)}
.btn-more{display:inline-block;margin:12px 0 0 5px;width:97px;height:27px;background:var(--blue);
  font-family:'Oswald',sans-serif;font-size:12px;color:var(--blue-ink);text-align:center;line-height:27px;text-decoration:none}

.divider{position:absolute;left:129px;top:884px;width:716px;height:1.5px;background:var(--choc)}
.tagline{position:absolute;left:129px;top:904px;width:716px;font-family:'Oswald',sans-serif;font-weight:400;
  font-size:33px;line-height:42px;color:var(--choc);text-align:center;white-space:nowrap;letter-spacing:.2px}
.occasions{position:absolute;left:129px;top:954px;width:716px;display:flex;align-items:center;justify-content:space-between}
.occasions span{font-size:19px;color:var(--choc);white-space:nowrap}
.occasions i{display:block;width:82px;height:1.5px;background:var(--choc)}

.footer{position:absolute;left:0;top:1003px;width:977px;height:197px;background:var(--choc)}
.footer h3{position:absolute;font-size:16px;color:var(--blue-light);white-space:nowrap}
.field{position:absolute;background:var(--white);border-radius:3px;font-family:'Open Sans',sans-serif;font-style:italic;
  font-size:11px;color:#777;padding:4px 10px}
.btn-send{position:absolute;width:59px;height:22px;background:linear-gradient(var(--cream),#d9cba3);
  font-family:'Open Sans',sans-serif;font-size:12px;color:var(--choc);text-align:center;line-height:22px;border-radius:2px}
.foot-links{position:absolute;left:134px;top:150px;display:flex;gap:12px}
.foot-links a{font-family:'Open Sans',sans-serif;font-size:10px;color:var(--white);text-decoration:none}
.copyright{position:absolute;left:134px;top:174px;font-family:'Open Sans',sans-serif;font-size:9.5px;color:var(--white)}
.social{position:absolute;left:710px;top:147px;display:flex;gap:14px}
.social span{width:23px;height:23px;border-radius:3px;background:var(--blue)}
</style>
</head>
<body>
  <div class="top-band"></div>
  <div class="scallop down"></div>

  <div class="ribbon-tail" style="left:73px;top:120px;width:57px;height:35px;clip-path:polygon(0 0,100% 0,100% 100%,0 100%,14% 50%)"></div>
  <div class="ribbon-tail" style="left:847px;top:120px;width:58px;height:35px;clip-path:polygon(0 0,100% 0,86% 50%,100% 100%,0 100%)"></div>

  <nav class="nav-bar nav-left">
    <a href="#">HOME</a><a href="#">ABOUT US</a><a href="#">PHOTO GALLEREY</a>
  </nav>
  <nav class="nav-bar nav-right">
    <a href="#">FLAVOUR MENU</a><a href="#">PRODUCTS</a><a href="#">CONTACT US</a>
  </nav>

  <div class="brand"><span class="brand-dot"></span><span class="brand-name">Amber Ladle Wishes</span></div>

  <div class="hero" role="img" aria-label="Photograph of a craft table with paper roses, pearls, crystals, feathers, ribbons and scissors for handmade cupcake toppers"></div>
  <div class="ribbon-tail" style="left:840px;top:474px;width:64px;height:35px;clip-path:polygon(0 0,100% 0,86% 50%,100% 100%,0 100%)"></div>
  <div class="hero-tag script">Lorem Ipsum</div>

  <h1 class="headline script">Creating Delicious Works of Art</h1>

  <section class="feature left">
    <h2>LOREM IPSUM DOLOR SIT AMET</h2>
    <p>Consectetuer adipiscing elit. Aenean commodo ligula eget dolor. Aenean massa. Cum sociis natoque penatibus et magnis dis parturient montes, nascetur ridiculus mus.</p>
    <p>Donec quam felis, ultricies nec, pellentesque eu, pretium quis, sem. Nulla consequat massa quis enim. Consectetuer adipiscing elit. Aenean commodo ligula eget dolor. Aenean massa. Cum sociis natoque penatibus et magnis dis parturient montes, nascetur ridiculus mus.</p>
    <a class="btn-more" href="#">READ MORE</a>
  </section>
  <section class="feature right">
    <h2>LOREM IPSUM DOLOR SIT AMET</h2>
    <p>Consectetuer adipiscing elit. Aenean commodo ligula eget dolor. Aenean massa. Cum sociis natoque penatibus et magnis dis parturient montes, nascetur ridiculus mus.</p>
    <p>Donec quam felis, ultricies nec, pellentesque eu, pretium quis, sem. Nulla consequat massa quis enim. Consectetuer adipiscing elit. Aenean commodo ligula eget dolor. Aenean massa. Cum sociis natoque penatibus et magnis dis parturient montes, nascetur ridiculus mus.</p>
    <a class="btn-more" href="#">READ MORE</a>
  </section>

  <div class="divider"></div>
  <h2 class="tagline">GOURMET CUPCAKES &amp; HANDMADE WRAPPERS &amp; TOPPERS</h2>
  <div class="occasions script">
    <span>Weddings</span><i></i><span>Christenings</span><i></i><span>Birthdays</span><i></i><span>Special Events</span>
  </div>

  <div class="scallop up"></div>
  <footer class="footer">
    <h3 class="script" style="left:130px;top:28px">Send us a Quick Message</h3>
    <div class="field" style="left:129px;top:55px;width:223px;height:22px">Email Address</div>
    <div class="field" style="left:129px;top:84px;width:223px;height:46px">Your Message</div>
    <div class="btn-send" style="left:360px;top:108px">Send</div>

    <h3 class="script" style="left:560px;top:28px">Join Our Newsletter</h3>
    <div class="field" style="left:560px;top:55px;width:222px;height:22px">Email Address</div>
    <div class="btn-send" style="left:791px;top:55px">Send</div>

    <nav class="foot-links">
      <a href="#">ABOUT US</a><a href="#">PHOTO GALLERY</a><a href="#">FLAVOUR MENU</a><a href="#">PRODUCTS</a><a href="#">CONTACT US</a>
    </nav>
    <p class="copyright">© 2011 All Rights Reserved. Amber Ladle Wishes</p>
    <div class="social"><span></span><span></span><span></span><span></span></div>
  </footer>
</body>
</html>
```